Can design for new all natural low calorie spiked lemonade

We need a clean but catchy can design for a new spiked lemonade that will be all natural, gluten free and low in calories. Open to any creative ideas ranging from designs such as using a lemonade stand to simple designs such as the example pictures that are uploaded. Looking for a can that just pops out right away on the shelf but also believe less is more as far as simplicity. The beverage is called Brightlow Spiked Lemonade, that features 3 flavors. Traditional Lemonade, Peach Lemonade and lastly Strawberry Lemonade.

Target Market(s)

21-55 years of age. 75% female, 25% male.

Colors

Designer to choose colors to be used in the design.

Requirements
Must have
• The brand name is Brightlow and it is a spiked lemonade so that should be catchy so the consumer knows what it is on first glance. Must say gluten free, all natural, and 150 calories on the front of the can. Would like some type of image on the front middle of the can. There are 3 flavors so the can should blend well with each fruit but not be different cans

```html
<!DOCTYPE html>
<html lang="en">
<head>
<meta charset="utf-8">
<title>Brightlow Spiked Lemonade — Can Labels</title>
<link href="https://fonts.googleapis.com/css2?family=Jura:wght@300;400&family=Oswald:wght@300;500;600&display=swap" rel="stylesheet">
<style>
  :root {
    --bg: #ffffff;
    --label-bg: #ffffff;
    --label-edge: #e6e8ea;
    --lemon: #5aa946;
    --peach: #f2864a;
    --peach-soft: #f5a06f;
    --berry: #e23a3f;
    --berry-deep: #9c2b2f;
    --count: #f07838;
    --count-berry: #e8463a;
  }
  * { box-sizing: border-box; margin: 0; padding: 0; }
  html, body { width: 1200px; height: 1200px; overflow: hidden; background: var(--bg); }
  .lineup {
    width: 1200px; height: 1200px;
    display: flex; justify-content: center; align-items: center; gap: 60px;
  }
  .label {
    width: 300px; height: 600px;
    background: var(--label-bg);
    border: 1px solid var(--label-edge);
    border-radius: 6px;
    display: flex; flex-direction: column; align-items: center;
    padding-top: 80px;
    font-family: "Jura", sans-serif;
  }
  .brand { font-size: 50px; font-weight: 300; line-height: 1; letter-spacing: 0; }
  .flavor {
    height: 24px; margin-top: 18px;
    font-size: 18px; font-weight: 400; letter-spacing: 4px; line-height: 24px;
  }
  .product { font-size: 36px; font-weight: 300; line-height: 1; margin-top: 4px; white-space: nowrap; }
  .fruit { width: 240px; height: 190px; margin-top: 24px; border-radius: 50%; }
  .claims {
    margin-top: 56px; width: 270px;
    display: grid; grid-template-columns: 1fr auto 1fr; align-items: end;
    font-family: "Oswald", sans-serif;
  }
  .claim { font-size: 19px; font-weight: 300; text-transform: uppercase; padding-bottom: 34px; }
  .claim.left { text-align: left; }
  .claim.right { text-align: right; }
  .calories { text-align: center; line-height: 1; padding: 0 6px; }
  .calories .count { font-size: 54px; font-weight: 600; display: block; }
  .calories .unit { font-size: 24px; font-weight: 500; display: block; margin-top: 4px; }

  .lemon .brand, .lemon .product, .lemon .claim { color: var(--lemon); }
  .lemon .count, .lemon .unit { color: var(--count); }
  .lemon .fruit { background: radial-gradient(circle at 45% 50%, #f7dc2e, #f1c81a 55%, #6aa83a 100%); }

  .peach .brand, .peach .product { color: var(--peach); }
  .peach .flavor { color: var(--peach-soft); }
  .peach .claim { color: #c9864f; }
  .peach .count { color: var(--berry); }
  .peach .unit { color: var(--count); }
  .peach .fruit { background: radial-gradient(circle at 45% 50%, #f4c04a, #e8654a 60%, #4f8a3c 100%); }

  .berry .brand, .berry .flavor { color: var(--berry); }
  .berry .product { color: var(--berry-deep); }
  .berry .claim { color: #b8433f; }
  .berry .count { color: var(--count-berry); }
  .berry .unit { color: var(--berry-deep); }
  .berry .fruit { background: radial-gradient(circle at 45% 55%, #e8485a, #c8303f 60%, #5a9a48 100%); }
</style>
</head>
<body>
  <main class="lineup">
    <section class="label lemon">
      <h1 class="brand">Brightlow</h1>
      <p class="flavor"></p>
      <h2 class="product">Spiked lemonade</h2>
      <div class="fruit" role="img" aria-label="Photo of whole and halved lemons with green leaves"></div>
      <div class="claims">
        <span class="claim left">All Natural</span>
        <span class="calories"><span class="count">150</span><span class="unit">CALORIES</span></span>
        <span class="claim right">Gluten Free</span>
      </div>
    </section>

    <section class="label peach">
      <h1 class="brand">Brightlow</h1>
      <p class="flavor">peach</p>
      <h2 class="product">Spiked lemonade</h2>
      <div class="fruit" role="img" aria-label="Photo of whole and halved peaches with green leaves"></div>
      <div class="claims">
        <span class="claim left">All Natural</span>
        <span class="calories"><span class="count">150</span><span class="unit">CALORIES</span></span>
        <span class="claim right">Gluten Free</span>
      </div>
    </section>

    <section class="label berry">
      <h1 class="brand">Brightlow</h1>
      <p class="flavor">strawberry</p>
      <h2 class="product">Spiked lemonade</h2>
      <div class="fruit" role="img" aria-label="Photo of whole and halved strawberries with leaves"></div>
      <div class="claims">
        <span class="claim left">All Natural</span>
        <span class="calories"><span class="count">150</span><span class="unit">CALORIES</span></span>
        <span class="claim right">Gluten Free</span>
      </div>
    </section>
  </main>
</body>
</html>
```